Company web site

Looking for a full responsive(mobile friendly) wordpress implementation

Some material is in the website -- brivanta.examplesite.test

But looking for a template more consistent with the logo design, and more future looking.

Target Market(s)

Enterprise Clients

Industry/Entity Type

It Company

Font styles to use
Sans Serif

Colors
33a6d7
0255a3
0455a3
cfdeed
85abd2
3176b5

Requirements
Must have
• about, contact information, partner page, success stories, customer testimonials. links to social presence.
• pricing information

```html
<!DOCTYPE html>
<html lang="en">
<head>
<meta charset="utf-8">
<title>Brivanta — Integrated IoT Solutions</title>
<link href="https://fonts.googleapis.com/css2?family=Montserrat:wght@300;400;500;600;700&family=Roboto:wght@300;400&display=swap" rel="stylesheet">
<style>
:root{
  --sky:#33a6d7;
  --navy:#0255a3;
  --brand:#3176b5;
  --mist:#cfdeed;
  --steel:#85abd2;
  --ink:#2b2f36;
  --text:#555a62;
  --muted:#8a9099;
  --panel:#f3f4f6;
  --white:#ffffff;
  --mountain:#4a5e78;
}
*{box-sizing:border-box;margin:0;padding:0}
html,body{width:1200px;height:3186px;overflow:hidden}
body{font-family:"Montserrat",sans-serif;color:var(--text);background:var(--white);position:relative}
section,header,footer{position:absolute;left:0;width:1200px}
.abs{position:absolute}

/* header + hero */
.hero{top:0;height:495px;background:linear-gradient(100deg,#5a96d6 0%,#4f8ed8 40%,#6c9fe0 70%,#8fb6ea 100%)}
.logo{left:60px;top:22px;font-weight:300;font-size:30px;letter-spacing:6px;color:var(--white)}
.nav{left:395px;top:28px;display:flex;gap:30px;font-size:14px;font-weight:500;color:var(--white)}
.nav a{color:inherit;text-decoration:none;padding-bottom:6px}
.nav a.active{border-bottom:2px solid var(--white)}
.signin{display:flex;align-items:center;gap:6px}
.hero-title{left:87px;top:185px;font-size:28px;font-weight:400;color:var(--white);line-height:1.3}
.hero-title b{font-weight:700}
.hero-copy{left:87px;top:268px;width:440px;font-size:13.5px;line-height:1.35;color:#eef4fb}
.btn-pill{display:inline-flex;align-items:center;justify-content:center;border-radius:24px;font-size:11px;font-weight:700;letter-spacing:1px;text-transform:uppercase}
.hero-btn{left:87px;top:358px;width:166px;height:38px;background:var(--brand);color:var(--white)}
.arrow{color:var(--white);font-size:34px}
.dashboard-shot{left:672px;top:115px;width:440px;height:360px;border-radius:10px;background:linear-gradient(180deg,#dfe4ea 0%,#c3ccd6 70%,#e9ecef 100%)}

/* about */
.about{top:495px;height:335px;background:var(--white)}
.section-title{font-size:28px;font-weight:400;color:var(--ink)}
.section-title b{color:var(--brand);font-weight:700}
.about .section-title{left:87px;top:50px;font-size:27px}
.title-rule{height:2px;width:50px;background:var(--brand)}
.about .title-rule{left:87px;top:90px}
.about-copy{left:87px;top:115px;width:450px;font-size:13.5px;line-height:1.4;color:var(--muted)}
.about-copy p+p{margin-top:14px}
.outline-btn{border:2px solid var(--brand);color:var(--ink);background:var(--white)}
.about-btn{left:87px;top:238px;width:166px;height:38px}
.globe-art{left:600px;top:0;width:512px;height:335px;background:radial-gradient(circle at 40% 70%,#3d5f86 0%,#1d3452 45%,#0c1627 100%)}

/* stories */
.stories{top:830px;height:500px}
.stories-band{left:0;top:0;width:1200px;height:270px;background:var(--panel)}
.centered{left:0;width:1200px;text-align:center}
.stories .section-title{top:48px}
.rule-center{left:575px;width:50px}
.stories .title-rule{top:90px}
.video-frame{left:270px;top:135px;width:662px;height:268px;background:var(--white);padding:4px;box-shadow:0 2px 8px rgba(0,0,0,.12)}
.video-still{width:100%;height:100%;background:linear-gradient(90deg,#3b3e44 0%,#6d6f73 45%,#4a4d52 100%);display:flex;align-items:center;justify-content:center}

/* pricing */
.pricing{top:1260px;height:560px}
.pricing .section-title{top:20px}
.pricing .title-rule{top:62px}
.plan{background:var(--panel);text-align:center;padding-top:48px}
.plan.featured{background:var(--white);box-shadow:0 4px 18px rgba(0,0,0,.14);padding-top:60px}
.plan-name{font-size:11px;font-weight:600;letter-spacing:1px;color:var(--ink);text-transform:uppercase}
.price{font-family:"Roboto",sans-serif;font-weight:300;color:var(--sky);font-size:56px;margin-top:16px;line-height:1}
.price sup{font-size:26px;vertical-align:14px;margin-right:6px}
.plan.featured .price{color:var(--navy);font-size:66px}
.price-rule{width:64px;height:1px;background:var(--mist);margin:20px auto 28px}
.features{list-style:none;font-size:11px;font-weight:500;letter-spacing:.6px;color:var(--text);text-transform:uppercase;line-height:27px}
.features b{font-weight:700}
.plan-btn{width:140px;height:38px;margin-top:22px}
.plan.featured .plan-btn{background:var(--brand);color:var(--white);border:none}

/* testimonial */
.testimonial{top:1860px;height:492px;background:linear-gradient(180deg,#4c6786 0%,#56708e 45%,#3d4f66 100%)}
.quote-mark{top:52px;font-size:90px;font-family:Georgia,serif;color:var(--white);line-height:1}
.quote-text{left:280px;top:128px;width:640px;text-align:center;font-style:italic;font-size:17px;line-height:1.6;color:var(--white)}
.avatar-line{left:250px;top:350px;width:700px;height:1px;background:rgba(255,255,255,.35)}
.avatar{border-radius:50%;border:3px solid rgba(255,255,255,.8);background:linear-gradient(180deg,#b9a58f,#7e6a58)}
.client-name{top:403px;font-size:17px;font-weight:700;color:var(--white)}
.client-role{top:428px;font-size:11px;color:var(--mist)}

/* partners */
.partners{top:2352px;height:276px}
.partners .section-title{left:87px;top:50px;font-size:27px}
.partner-nav{left:1055px;top:58px;color:var(--ink);font-size:18px;display:flex;gap:8px;align-items:center}
.partner-row{left:87px;top:128px;display:flex;gap:28px}
.partner-tile{width:183px;height:92px;background:var(--panel);display:flex;align-items:center;justify-content:center;gap:8px;font-size:20px;font-weight:600;color:var(--navy)}
.partner-tile i{width:14px;height:14px;background:var(--sky);display:block}

/* contact */
.contact{top:2628px;height:364px;background:var(--brand);color:var(--white)}
.contact .section-title{color:var(--white);font-size:27px}
.contact .section-title b{color:var(--white)}
.contact-info{left:176px;top:125px;font-size:13.5px;line-height:1.45}
.phone{left:176px;top:190px;font-size:19px;font-weight:600;display:flex;align-items:center;gap:6px}
.email{left:176px;top:222px;font-size:13.5px}
.socials{left:176px;top:270px;display:flex;gap:10px}
.socials span{width:32px;height:32px;border-radius:50%;border:2px solid var(--white);display:block}
.socials span.on{background:var(--white)}

.footer{top:2992px;height:194px;background:#eeeff1}
.footer-logo{left:176px;top:24px;font-weight:300;font-size:42px;letter-spacing:7px;color:var(--brand)}
.footer-rule{left:176px;top:110px;width:880px;height:1px;background:#d4d7dc}
.copyright{left:176px;top:127px;font-size:12px;color:var(--muted)}
.footer-links{left:176px;top:150px;font-size:12px;color:var(--muted);display:flex;gap:8px}
.footer-links .current{color:var(--brand);text-decoration:underline}
.to-top{left:1003px;top:127px}

.form-card{left:615px;top:2748px;width:410px;height:314px;background:var(--white);box-shadow:0 4px 16px rgba(0,0,0,.15);padding:18px 20px}
.field{height:36px;border:1px solid #dcdfe3;margin-bottom:10px;padding:9px 10px;font-size:10px;color:var(--muted)}
.field.message{height:84px}
.send-btn{width:128px;height:34px;background:var(--brand);color:var(--white);gap:6px;margin-top:6px}
</style>
</head>
<body>

<header class="hero">
  <div class="abs logo">BRIVANTA</div>
  <nav class="abs nav">
    <a class="active" href="#">Home</a><a href="#">About Us</a><a href="#">Platform</a><a href="#">Pricing</a><a href="#">Partners</a><a href="#">Blog</a><a href="#">Contact Us</a>
    <a class="signin" href="#"><svg width="16" height="16" viewBox="0 0 16 16"><path d="M9 2h5v12H9" fill="none" stroke="#fff" stroke-width="2"/><path d="M1 8h8M6 5l3 3-3 3" fill="none" stroke="#fff" stroke-width="2"/></svg>SIGN IN</a>
  </nav>
  <h1 class="abs hero-title">Focus on <b>your product.</b><br>We manage the integrations.</h1>
  <p class="abs hero-copy">With Brivanta you pick-and-choose the features your customers want. And get all the tools you need to operate your IoT business.</p>
  <a class="abs btn-pill hero-btn">Explore More</a>
  <div class="abs arrow" style="left:14px;top:245px">&larr;</div>
  <div class="abs arrow" style="left:1155px;top:245px">&rarr;</div>
  <div class="abs dashboard-shot" role="img" aria-label="Desktop monitor showing the platform dashboard with a device map and activity chart"></div>
</header>

<section class="about">
  <h2 class="abs section-title">About <b>Us</b></h2>
  <div class="abs title-rule"></div>
  <div class="abs about-copy">
    <p>Founded in 2016 by industry veterans. Brivanta is geared to provide integrated solutions for the IoT industry</p>
    <p>With a off-shore development center in Eastern Europe, Brivanta is positioned to provided development</p>
  </div>
  <a class="abs btn-pill outline-btn about-btn">Discover More</a>
  <div class="abs globe-art" role="img" aria-label="Night view of the globe with glowing network connections"></div>
</section>

<section class="stories">
  <div class="abs stories-band"></div>
  <h2 class="abs centered section-title">Success <b>Stories</b></h2>
  <div class="abs title-rule rule-center"></div>
  <div class="abs video-frame">
    <div class="video-still" role="img" aria-label="Customer success story video still of a client in an office">
      <svg width="48" height="48" viewBox="0 0 48 48"><circle cx="24" cy="24" r="21" fill="none" stroke="#fff" stroke-width="3"/><path d="M19 15l14 9-14 9z" fill="#fff"/></svg>
    </div>
  </div>
</section>

<section class="pricing">
  <h2 class="abs centered section-title">Our <b>Pricing</b></h2>
  <div class="abs title-rule rule-center"></div>
  <div class="abs plan" style="left:175px;top:130px;width:265px;height:370px">
    <div class="plan-name">Basic Plan</div>
    <div class="price"><sup>$</sup>29</div>
    <div class="price-rule"></div>
    <ul class="features"><li>500GB Storage Space</li><li><b>Free</b> Domain</li><li><b>20</b> Email Addresses</li></ul>
    <a class="btn-pill outline-btn plan-btn">Get Started</a>
  </div>
  <div class="abs plan" style="left:762px;top:130px;width:265px;height:370px">
    <div class="plan-name">Premium Plan</div>
    <div class="price"><sup>$</sup>199</div>
    <div class="price-rule"></div>
    <ul class="features"><li>500GB Storage Space</li><li><b>Free</b> Domain</li><li><b>20</b> Email Addresses</li></ul>
    <a class="btn-pill outline-btn plan-btn">Get Started</a>
  </div>
  <div class="abs plan featured" style="left:438px;top:102px;width:324px;height:428px">
    <div class="plan-name">Standard Plan</div>
    <div class="price"><sup>$</sup>59</div>
    <div class="price-rule"></div>
    <ul class="features"><li>700GB Storage Space</li><li><b>Free</b> Domain</li><li><b>30</b> Email Addresses</li><li><b>24/7</b> Support</li></ul>
    <a class="btn-pill outline-btn plan-btn">Get Started</a>
  </div>
</section>

<section class="testimonial" role="img" aria-label="Snowy mountain range under a cloudy sky">
  <div class="abs centered quote-mark">&ldquo;</div>
  <p class="abs quote-text">Lorem ipsum dolor sit amet, consectetur adipiscing elit. Suspendisse eleifend id metus id fringilla. Phasellus euismod commodo felis, sit amet egestas dui euismod vitae. Aenean venenatis malesuada nisi sit amet hendrerit.</p>
  <div class="abs arrow" style="left:175px;top:150px">&larr;</div>
  <div class="abs arrow" style="left:993px;top:150px">&rarr;</div>
  <div class="abs avatar-line"></div>
  <div class="abs avatar" style="left:485px;top:327px;width:48px;height:48px" role="img" aria-label="Client portrait"></div>
  <div class="abs avatar" style="left:562px;top:308px;width:78px;height:78px" role="img" aria-label="Client portrait"></div>
  <div class="abs avatar" style="left:668px;top:327px;width:48px;height:48px" role="img" aria-label="Client portrait"></div>
  <div class="abs centered client-name">Marek Dolan</div>
  <div class="abs centered client-role">Happy Client</div>
</section>

<section class="partners">
  <h2 class="abs section-title">Our <b>Partners</b></h2>
  <div class="abs partner-nav">&larr; <span style="font-size:11px">|</span> <span style="color:var(--brand)">&rarr;</span></div>
  <div class="abs partner-row">
    <div class="partner-tile"><i></i>Nimbora</div>
    <div class="partner-tile"><i></i>Vextrel</div>
    <div class="partner-tile"><i></i>Quadrine</div>
    <div class="partner-tile"><i></i>Stratavo</div>
    <div class="partner-tile"><i></i>Helixon</div>
  </div>
</section>

<section class="contact">
  <h2 class="abs section-title" style="left:176px;top:50px">Contact <b>Us</b></h2>
  <h2 class="abs section-title" style="left:615px;top:50px">Get in <b>Touch</b></h2>
  <div class="abs contact-info">Brivanta<br>418 Harbor Lane&nbsp; Fairview,<br>CA 90210</div>
  <div class="abs phone">Call Us <svg width="16" height="16" viewBox="0 0 16 16"><path d="M3 1h3l1 4-2 1c1 2 3 4 5 5l1-2 4 1v3c0 1-1 2-2 2C7 15 1 9 1 3c0-1 1-2 2-2z" fill="#fff"/></svg>+1-(555) 014-2290</div>
  <div class="abs email">info@brivanta.test</div>
  <div class="abs socials" aria-label="Social profiles"><span></span><span class="on"></span><span></span><span></span></div>
</section>

<footer class="footer">
  <div class="abs footer-logo">BRIVANTA</div>
  <div class="abs footer-rule"></div>
  <div class="abs copyright">&copy; 2017 Brivanta. All Rights Reserved.</div>
  <div class="abs footer-links"><span>Login</span>/<span class="current">Support</span>/<span>Contact</span>/<span>Privacy Policy</span></div>
  <svg class="abs to-top" width="20" height="22" viewBox="0 0 20 22"><path d="M10 16V3M4 9l6-6 6 6M2 20h16" fill="none" stroke="#3176b5" stroke-width="2.4"/></svg>
</footer>

<form class="abs form-card">
  <div class="field">Name:</div>
  <div class="field">Phone:</div>
  <div class="field">Email:</div>
  <div class="field message">Massage:</div>
  <button type="button" class="btn-pill send-btn" style="border:none;font-family:inherit">
    <svg width="12" height="12" viewBox="0 0 12 12"><path d="M1 6l10-5-3 10-2-4z" fill="#fff"/></svg>Send
  </button>
</form>

</body>
</html>
```